Fashion Design Business Card

I need a new business card designed for a new fashion company. I have attached what I have currently designed. I want it more feminine looking, the logo needs to be gold. I want it simple, feminine and stylish. Please give me some different ideas with the fonts.
Updates

I need to send the design we currently have, as we have worked out the logo.
You also need all of our details
Industry/Entity Type
Fashion
Look and feel
Each slider illustrates characteristics of the customer's brand and the style your logo design should communicate.

```html
<!DOCTYPE html>
<html lang="en">
<head>
<meta charset="utf-8">
<title>Mirela Ashcombe – Business Card</title>
<link href="https://fonts.googleapis.com/css2?family=Abel&display=swap" rel="stylesheet">
<style>
  :root {
    --paper: #ffffff;
    --ink: #1c1c1c;
    --muted: #8a8a8a;
    --frame: #2a2a2a;
    --gold-deep: #ffd200;
    --gold-mid: #ffe31a;
    --gold-light: #fff84a;
    --gold-mark: #e9b800;
    --ghost: rgba(255, 255, 255, 0.28);
  }
  html, body {
    margin: 0;
    padding: 0;
    width: 1200px;
    height: 901px;
    overflow: hidden;
    background: var(--paper);
    font-family: "Abel", "Arial Narrow", sans-serif;
  }
  .board {
    position: absolute;
    left: 4px;
    top: 4px;
    width: 1188px;
    height: 889px;
    border: 2px solid var(--frame);
    border-radius: 14px;
    background: var(--paper);
  }
  .gold-surface {
    background: linear-gradient(135deg,
      var(--gold-deep) 0%, var(--gold-light) 18%, var(--gold-deep) 34%,
      var(--gold-light) 52%, var(--gold-deep) 70%, var(--gold-light) 86%,
      var(--gold-mid) 100%);
  }
  .card {
    position: absolute;
    border: 2px solid var(--ink);
    overflow: hidden;
  }
  .card--front {
    left: 56px;
    top: 126px;
    width: 384px;
    height: 670px;
    border-radius: 24px;
    background: var(--paper);
  }
  .front__identity {
    position: absolute;
    left: 0; top: 0;
    width: 100%;
    height: 328px;
    text-align: center;
  }
  .brand-mark {
    position: absolute;
    left: 0; right: 0;
    top: 96px;
    display: flex;
    justify-content: center;
    align-items: center;
    gap: 12px;
    color: var(--gold-mark);
    font-size: 40px;
    letter-spacing: 1px;
  }
  .brand-mark__dot {
    width: 14px;
    height: 14px;
    border-radius: 50%;
    background: var(--gold-mark);
  }
  .person-name {
    position: absolute;
    left: 0; right: 0;
    top: 232px;
    margin: 0;
    font-size: 37px;
    font-weight: 400;
    letter-spacing: 1.5px;
    color: var(--ink);
  }
  .person-role {
    position: absolute;
    left: 0; right: 0;
    top: 280px;
    margin: 0;
    font-size: 17px;
    font-style: italic;
    letter-spacing: 1.5px;
    color: var(--muted);
  }
  .front__divider {
    position: absolute;
    left: 0;
    top: 328px;
    width: 100%;
    height: 5px;
    background: var(--ink);
  }
  .front__contact {
    position: absolute;
    left: 0;
    top: 333px;
    width: 100%;
    height: 337px;
  }
  .contact-list {
    position: absolute;
    left: 0; right: 0;
    top: 60px;
    margin: 0;
    padding: 0;
    list-style: none;
    text-align: center;
    font-size: 20px;
    letter-spacing: 1.5px;
    line-height: 30px;
    color: var(--ink);
  }
  .ghost-name {
    position: absolute;
    color: var(--ghost);
    white-space: nowrap;
  }
  .ghost-name--small {
    right: 22px;
    bottom: 20px;
    font-size: 16px;
  }
  .card--back {
    left: 500px;
    top: 255px;
    width: 670px;
    height: 384px;
    border-radius: 22px;
  }
  .ghost-name--large {
    left: 0; right: 0;
    top: 70px;
    text-align: center;
    font-size: 70px;
  }
  .website {
    position: absolute;
    left: 0; right: 0;
    top: 176px;
    margin: 0;
    text-align: center;
    font-size: 40px;
    font-style: italic;
    letter-spacing: 5px;
    color: var(--ink);
  }
</style>
</head>
<body>
  <main class="board">
    <section class="card card--front" aria-label="Business card front">
      <header class="front__identity">
        <div class="brand-mark">
          <span class="brand-mark__dot"></span>
          <span class="brand-mark__name">Mirela Ashcombe</span>
        </div>
        <h1 class="person-name">Mirela Ashcombe</h1>
        <p class="person-role">Fashion Designer</p>
      </header>
      <div class="front__divider"></div>
      <div class="front__contact gold-surface">
        <ul class="contact-list">
          <li class="contact-list__phone">Phone: 0400123456</li>
          <li class="contact-list__email">mirela@mirelaashcombe.com</li>
        </ul>
        <span class="ghost-name ghost-name--small">Mirela Ashcombe</span>
      </div>
    </section>

    <section class="card card--back gold-surface" aria-label="Business card back">
      <span class="ghost-name ghost-name--large">Mirela Ashcombe</span>
      <p class="website">www.mirelaashcombe.com</p>
    </section>
  </main>
</body>
</html>
```